依頼詳細
★TOPラフ案について

・トップページの掲載内容はエクセルで作成した資料を添付しました。
仕様はワイヤーフレームのみですので、掲載情報が正しければ、お好きなデザインにて調整していただいて構いません。

掲載している情報のレイアウト通りではなくて大丈夫ですので
皆さまの感性にてお願いいたします。

・配置やデザイン等はアレンジしていただいて構いません。

・サイズは横幅2000pxで制作をお願いします。
縦に制限はありません。(コンテンツ幅は1100px~1200px内でお願いします。)
レスポンシブデザインのサイトで、bootstrap4を利用し、コーディングする予定になります。

・カラーイメージ
白を基調としてサブに青系、ワンポイントに赤色にてお願いします。

・ロゴ画像はヘッダーに入れる予定です。
(ロゴは青色(#00008B)で会社名ローマ字表示となります。頭文字は赤色(#FF3737)です。)

・デザインイメージ
誠実なデザインのイメージです。

デザイン選定後、決定した方には、正式な社名や連絡先を入れた修正をお願いしたいのと、
その他常識範囲で修正を依頼することもあります。
※以後、希望があれば中ページ作成及び他の案件コンテンツも継続してご依頼可能です。
ページ数
1ページ
希望イメージ
シンプル 複雑
単色 カラフル
暗い 明るい
日常 高級
遊び心 厳粛
未来的 伝統的
女性的 男性的
希望する色
青系
納品ファイル
• 高解像度JPG (.jpg)
• フォトショップ形式 (.psd)
補足説明
※ワイヤーフレーム通りのデザインでなくて、構いません。
メインビジュアル、素材などもお好みでデザインいただいて問題ございません。

仕様素材につきましてはZELNO定額素材内で使用可能な素材をご選択いただいてご使用ください。
(添付したデータ内にない素材でもご利用OKです。
その際は選定後素材№をお知らせください。)
■ 選んだ理由

依頼したイメージに沿ったデザインを作成いただけたためこちらのデザインに決めさせていただきました。

■ 提案者全員のお礼・コメント

多くの提案をいただき本当にありがとうございました。
次回の依頼の際も是非提案いただけますようお願いいたします。

```html
<!DOCTYPE html>
<html lang="ja">
<head>
<meta charset="utf-8">
<title>SMILECRAFT INC.</title>
<link rel="stylesheet" href="https://fonts.googleapis.com/css2?family=Montserrat:wght@500;700;800&family=Noto+Sans+JP:wght@400;500;700&display=swap">
<style>
:root{
  --navy:#0d1a6e;
  --navy-deep:#0a145a;
  --blue:#2a4fb8;
  --red:#ff3737;
  --ink:#1c2240;
  --white:#ffffff;
  --tint:#eef2f9;
  --line:#d5dcea;
  --muted:#7f8aa6;
  --text:#333a52;
}
*{margin:0;padding:0;box-sizing:border-box}
html,body{width:1200px;height:3833px;overflow:hidden}
body{position:relative;background:var(--white);color:var(--ink);font-family:"Noto Sans JP",sans-serif}
.abs{position:absolute}
.photo{position:absolute}
.heading{font-family:"Montserrat",sans-serif;font-weight:700;font-size:44px;letter-spacing:1px;color:var(--navy)}
.heading::after{content:"";display:block;width:40px;height:4px;background:var(--red);margin-top:10px}
.btn{position:absolute;width:210px;height:48px;background:var(--navy);color:var(--white);font-family:"Montserrat",sans-serif;font-weight:700;font-size:14px;letter-spacing:1px;display:flex;align-items:center;justify-content:center}
.body-text{font-size:18px;line-height:1.95;color:var(--text)}

/* hero */
.hero-photo{left:0;top:0;width:720px;height:630px;background:linear-gradient(135deg,#cfc9c0 0%,#b7a99a 40%,#e6e2dc 100%)}
.hero-panel{left:600px;top:0;width:600px;height:730px;background:var(--navy)}
.brand{left:42px;top:48px;display:flex;align-items:center;gap:10px;color:var(--white);font-family:"Montserrat",sans-serif;font-weight:800;font-size:34px;letter-spacing:1px}
.brand-mark{width:24px;height:24px;background:var(--red);border-radius:50%}
.menu{left:1070px;top:46px;display:flex;align-items:center;gap:10px;color:var(--white);font-family:"Montserrat",sans-serif;font-weight:700;font-size:15px}
.hero-sub{left:728px;top:100px;color:var(--white);font-size:26px;font-weight:500;letter-spacing:1px}
.hero-co{left:728px;top:140px;color:var(--white);font-family:"Montserrat",sans-serif;font-weight:800;font-size:30px}
.hero-title{left:724px;top:190px;color:var(--white);font-family:"Montserrat",sans-serif;font-weight:800;font-size:96px;line-height:1.15;letter-spacing:2px}
.hero-title em{font-style:normal;color:var(--red)}

/* about */
.about-photo{left:0;top:885px;width:1200px;height:800px;background:linear-gradient(180deg,#c9ccd4 0%,#7f8799 45%,#3a4258 100%)}
.about-card{left:60px;top:1030px;width:775px;height:515px;background:var(--white);padding:62px 40px 0 42px}
.about-card .body-text{margin-top:26px}

/* works & culture */
.feature-bg{left:0;top:1685px;width:1200px;height:835px;background:var(--tint)}
.feature{position:absolute;top:1840px;width:530px}
.feature .photo{position:relative;width:530px;height:360px;margin-top:22px}
.feature p{margin-top:40px;font-size:18px;color:var(--text)}
.feature .btn{position:relative;margin-top:30px}
.works-photo{background:linear-gradient(135deg,#dfe3e8 0%,#b9c0ca 50%,#8e97a4 100%)}
.culture-photo{background:linear-gradient(180deg,#6a6f82 0%,#c49a6c 60%,#2a2320 100%)}

/* topics */
.topics-head{left:40px;top:2590px}
.topic{position:absolute;left:245px;width:915px;height:108px;border-bottom:1px solid var(--line);padding-top:18px}
.topic time{display:block;font-family:"Montserrat",sans-serif;font-size:11px;color:var(--muted)}
.topic span{display:block;margin-top:8px;font-size:17px;font-weight:500;color:var(--ink)}

/* contact */
.contact-bg{left:0;top:3110px;width:1200px;height:660px;background:var(--tint)}
.contact-photo{left:570px;top:3215px;width:590px;height:400px;background:linear-gradient(160deg,#9fb6c8 0%,#7c7468 50%,#4a4036 100%)}
.footer{left:0;top:3770px;width:1200px;height:63px;background:var(--navy-deep);color:#c9d1ea;font-family:"Montserrat",sans-serif;font-size:12px;display:flex;align-items:center;justify-content:center}
</style>
</head>
<body>

<div class="photo hero-photo" role="img" aria-label="Mother holding a smiling baby in a bright kitchen"></div>
<div class="abs hero-panel"></div>
<div class="abs brand"><span class="brand-mark"></span>SMILECRAFT INC.</div>
<div class="abs menu">
  <svg width="26" height="18" viewBox="0 0 26 18"><g stroke="#fff" stroke-width="2.4"><line x1="0" y1="2" x2="26" y2="2"/><line x1="0" y1="9" x2="26" y2="9"/><line x1="0" y1="16" x2="26" y2="16"/></g></svg>MENU
</div>
<div class="abs hero-sub">デザインで人を笑顔にする会社</div>
<div class="abs hero-co">SMILECRAFT INC.</div>
<h1 class="abs hero-title">DESIGN<br>FOR<br>SMILE<em>.</em></h1>

<section>
  <div class="photo about-photo" role="img" aria-label="City skyline with a bridge and river"></div>
  <div class="abs about-card">
    <h2 class="heading">ABOUT US</h2>
    <p class="body-text">SMILECRAFTは、デザインで人を笑顔にする会社。<br>なんでもない日常に少しのワクワクと遊び心を提供します。実際には世界<br>を変える力がある。デザインには人を幸せにする力がある。毎日に幸せを<br>感じて生きていきたい。<br>SMILECRAFTの社名にはそんな想いが込められています。</p>
  </div>
  <div class="btn" style="left:102px;top:1440px">READ MORE</div>
</section>

<section>
  <div class="abs feature-bg"></div>
  <div class="feature" style="left:40px">
    <h2 class="heading">WORKS</h2>
    <div class="photo works-photo" role="img" aria-label="People seated around a bright open office seen from above"></div>
    <p>SMILECRAFTの制作実績を紹介します。</p>
    <div class="btn">READ MORE</div>
  </div>
  <div class="feature" style="left:630px">
    <h2 class="heading">CULTURE</h2>
    <div class="photo culture-photo" role="img" aria-label="Silhouettes of a team jumping at sunset"></div>
    <p>SMILECRAFTの社内文化について紹介します。</p>
    <div class="btn">READ MORE</div>
  </div>
</section>

<section>
  <h2 class="abs heading topics-head">LATEST TOPICS</h2>
  <div class="topic" style="top:2670px"><time>2019.02.14</time><span>イベントレポート「VRクリエイター座談会 ～5Gの次に来るもの～」</span></div>
  <div class="topic" style="top:2778px"><time>2019.01.22</time><span>プレスリリースのお知らせ NORTHWAVE RECORDS</span></div>
  <div class="topic" style="top:2886px"><time>2019.01.04</time><span>新年明けましておめでとうございます</span></div>
  <div class="btn" style="left:950px;top:3025px">READ MORE</div>
</section>

<section>
  <div class="abs contact-bg"></div>
  <h2 class="abs heading" style="left:40px;top:3215px">CONTACT</h2>
  <p class="abs body-text" style="left:40px;top:3315px">制作の依頼、取材の依頼、IRや採用についての<br>連絡・お問い合わせはコンタクトページから承<br>っております。<br>まずはお気軽にご連絡ください。担当者から改<br>めて返信いたします。</p>
  <div class="btn" style="left:40px;top:3565px">READ MORE</div>
  <div class="photo contact-photo" role="img" aria-label="Group of friends sitting together outdoors"></div>
</section>

<footer class="abs footer">©2018 SMILECRAFT INC.</footer>

</body>
</html>
```